Leaflets
We supply stone and solid surfaces to the trade and project manage its installation
Project: Leaflets
Leaflets - Construction
Creative Brief
Construction
Architects, Interior designers, property developers, kitchen and bathroom designers, shopfitters Our offer is mainly business to business. Our branding and images are corporate and our content (wording) is more casual (which is what makes us different from the competition)
A leaflet with our branding, logos and fonts to be used as an introduction to our clients mainly targeted trough site visits and by posting samples. Images and branding available on request.

```html
<!DOCTYPE html>
<html lang="en">
<head>
<meta charset="utf-8">
<title>Trelvax Leaflets</title>
<link href="https://fonts.googleapis.com/css2?family=Open+Sans:wght@400;700&display=swap" rel="stylesheet">
<style>
:root{
  --purple:#6b2d8f;
  --purple-dark:#4f1f6b;
  --green:#8cc63f;
  --paper:#ffffff;
  --ink:#5a5a5a;
  --bg:#ffffff;
  --label:#777777;
}
*{box-sizing:border-box;margin:0;padding:0}
html,body{width:1200px;height:250px;overflow:hidden;background:var(--bg);font-family:"Open Sans",Arial,sans-serif}
.board{position:relative;width:1200px;height:250px}
.label{position:absolute;font-size:5px;letter-spacing:.5px;color:var(--label);text-transform:uppercase}
.sheet{position:absolute;background:var(--paper);box-shadow:0 0 2px rgba(0,0,0,.35);overflow:hidden}
.photo{position:absolute;background:linear-gradient(135deg,#dedbd7,#aaa59f 60%,#7d7872)}
.band{position:absolute;background:var(--purple);color:#fff}
.accent{position:absolute;background:var(--green)}
.copy{position:absolute;font-size:2.6px;line-height:3.4px;color:var(--ink);text-align:justify}
.copy p+p{margin-top:1.6px}
.band .copy{color:#fff}
.head{position:absolute;font-size:4px;font-weight:700;color:var(--purple);white-space:nowrap}
.brand{position:absolute;display:flex;align-items:center;gap:2px;font-weight:700;color:var(--purple);white-space:nowrap}
.brand i{display:block;background:var(--purple)}
.band .brand{color:#fff}
.band .brand i{background:#fff}
.panel{position:absolute;top:0;height:100%}
.ticks{position:absolute;list-style:none;font-size:2.6px;line-height:3.6px;color:var(--ink)}
.ticks li::before{content:"\2713";color:var(--green);font-weight:700;margin-right:1.5px}
.band .ticks{color:#fff}
</style>
</head>
<body>
<div class="board">

  <!-- Single flyer -->
  <span class="label" style="left:34px;top:3px">Front</span>
  <span class="label" style="left:108px;top:3px">Back</span>

  <div class="sheet" style="left:6px;top:10px;width:70px;height:100px">
    <div class="photo" role="img" aria-label="Modern kitchen with stone worktops" style="left:0;top:0;width:70px;height:42px"></div>
    <div class="band" style="left:0;top:42px;width:70px;height:24px">
      <div style="position:absolute;left:4px;top:3px;font-size:4.4px;font-weight:700">Stone &amp; Solid Surfaces</div>
      <div class="copy" style="left:4px;top:9px;width:62px">Supplied to the trade and fitted by our own team. We manage every step of the job, from the first template to the final polish, so you can get on with yours.</div>
    </div>
    <div class="accent" style="left:0;top:66px;width:70px;height:1.5px"></div>
    <ul class="ticks" style="left:4px;top:69px;width:62px">
      <li>Granite, quartz and marble</li>
      <li>Solid surfaces cut to size</li>
      <li>Templating and fitting</li>
      <li>Full project management</li>
    </ul>
    <div class="brand" style="left:4px;top:87px;font-size:6px"><i style="width:5px;height:5px"></i>Trelvax</div>
    <div class="copy" style="left:38px;top:88px;width:28px;text-align:right">0100 200 300<br>trelvax.example</div>
  </div>

  <div class="sheet" style="left:80px;top:10px;width:70px;height:100px">
    <div class="head" style="left:4px;top:3px">Who we are</div>
    <div class="copy" style="left:4px;top:8.5px;width:62px">
      <p>A friendly team supplying stone and solid surfaces to architects, designers and builders across the region. We like to keep things relaxed, but our work is always spot on.</p>
      <p>Every order is handled by one project manager who stays with you from start to end.</p>
    </div>
    <div class="photo" role="img" aria-label="Bathroom vanity in solid surface" style="left:4px;top:33px;width:30px;height:20px"></div>
    <div class="photo" role="img" aria-label="Stone kitchen island" style="left:36px;top:33px;width:30px;height:20px"></div>
    <div class="head" style="left:4px;top:56px">What we do</div>
    <div class="copy" style="left:4px;top:61.5px;width:62px">
      <p>Templating, fabrication and fitting, all project managed so you don't have to chase anyone. We work with kitchens, bathrooms, shops, hotels and offices, big or small.</p>
      <p>Ask for samples or a site visit and we will come to you.</p>
    </div>
    <div class="band" style="left:0;top:88px;width:70px;height:12px">
      <div class="brand" style="left:4px;top:3.5px;font-size:5px"><i style="width:4px;height:4px"></i>Trelvax</div>
      <div class="copy" style="left:38px;top:2.5px;width:28px;text-align:right">0100 200 300<br>trelvax.example</div>
    </div>
  </div>

  <!-- Trifold -->
  <span class="label" style="left:255px;top:40px">Front</span>
  <span class="label" style="left:462px;top:40px">Inside</span>

  <div class="sheet" style="left:165px;top:48px;width:204px;height:80px">
    <div class="panel" style="left:0;width:68px">
      <div class="head" style="left:4px;top:3px">Our projects</div>
      <div class="copy" style="left:4px;top:8.5px;width:60px">
        <p>Kitchens, bathrooms, shops, hotels and offices, all finished in stone and solid surfaces. We have worked with developers on large sites and with designers on one-off homes.</p>
        <p>Whatever the size, you get the same care, the same clear prices and a fitting team that turns up on time and leaves the site clean.</p>
      </div>
      <div class="photo" role="img" aria-label="Fitted kitchen project" style="left:4px;top:40px;width:60px;height:35px"></div>
    </div>
    <div class="band panel" style="left:68px;width:68px">
      <div class="brand" style="left:8px;top:24px;font-size:8px"><i style="width:6px;height:6px"></i>Trelvax</div>
      <div class="copy" style="left:8px;top:36px;width:52px">Stone and solid surfaces for the trade.</div>
      <div class="copy" style="left:8px;top:60px;width:52px">Unit 4, Millbrook Park<br>Call 0100 200 300<br>hello@trelvax.example</div>
    </div>
    <div class="panel" style="left:136px;width:68px">
      <div class="brand" style="left:10px;top:14px;font-size:9px"><i style="width:7px;height:7px"></i>Trelvax</div>
      <div class="copy" style="left:10px;top:27px;width:50px">Supply and fit, made simple.</div>
      <div class="accent" style="left:0;top:40px;width:68px;height:2px"></div>
      <div class="photo" role="img" aria-label="Stone worktop close-up" style="left:0;top:42px;width:68px;height:38px"></div>
    </div>
  </div>

  <div class="sheet" style="left:375px;top:48px;width:204px;height:80px">
    <div class="panel" style="left:0;width:68px">
      <div class="photo" role="img" aria-label="Kitchen interior" style="left:0;top:0;width:68px;height:28px"></div>
      <div class="accent" style="left:0;top:28px;width:68px;height:2px"></div>
      <div class="head" style="left:4px;top:33px">Hello</div>
      <div class="copy" style="left:4px;top:38.5px;width:60px">
        <p>We keep things simple: great materials, clear prices and fitters who turn up on time. No jargon, no fuss, just good work done well.</p>
        <p>Tell us about your project and we will send samples, a quote and a date for templating, usually within the week.</p>
      </div>
    </div>
    <div class="panel" style="left:68px;width:68px">
      <div class="head" style="left:4px;top:3px">Materials</div>
      <div class="copy" style="left:4px;top:8.5px;width:60px">Granite, quartz, marble and solid surfaces in many colours and finishes, all cut and polished in our own workshop.</div>
      <div class="photo" role="img" aria-label="Stone samples" style="left:4px;top:23px;width:60px;height:28px"></div>
      <ul class="ticks" style="left:4px;top:54px;width:60px">
        <li>Worktops and islands</li>
        <li>Vanity tops and basins</li>
        <li>Shower trays and wall panels</li>
        <li>Reception desks and counters</li>
        <li>Window sills and hearths</li>
      </ul>
    </div>
    <div class="panel" style="left:136px;width:68px">
      <div class="photo" role="img" aria-label="Bathroom with solid surface basin" style="left:0;top:0;width:68px;height:28px"></div>
      <div class="accent" style="left:0;top:28px;width:68px;height:2px"></div>
      <div class="head" style="left:4px;top:33px">Get in touch</div>
      <div class="copy" style="left:4px;top:38.5px;width:60px">
        <p>Ask for samples or book a site visit today. We cover the whole region and are happy to meet on site, in your studio or at our showroom.</p>
        <p>Call 0100 200 300<br>hello@trelvax.example<br>trelvax.example</p>
      </div>
    </div>
  </div>

</div>
</body>
</html>
```